Benefit Porter

Need home page design for new website. The winner will have the opportunity to design the entire site.

I have attached 3 files.

1) Sort of a site map. PLEASE do not design the home page based on this wire frame. Be creative and use your expertise.

2) Tagline and Copy for the home page. Please just greek in or make up copy for areas that do not have copy at this time.

3) The logo.
Updates

Hi everyone, I am sorry for the delay. I have been out of town on unexpected business. I will make a decision this week. Thank you all for the great designs. Dale

```html
<!DOCTYPE html>
<html lang="en">
<head>
<meta charset="utf-8">
<title>Benefit Porter</title>
<link href="https://fonts.googleapis.com/css2?family=Anton&family=Arimo:wght@400;700&family=Lato:ital,wght@0,400;0,700;1,400&display=swap" rel="stylesheet">
<style>
:root{
  --blue:#1a6f9a;
  --green:#2da84a;
  --ink:#222;
  --text:#444;
  --band:#e6e6e6;
  --footer:#2b2b2b;
  --footer-bar:#1a6f9a;
  --rule:#c9c9c9;
}
*{margin:0;padding:0;box-sizing:border-box}
html,body{width:884px;height:1200px;overflow:hidden;background:#fff}
body{position:relative;font-family:'Lato',sans-serif;color:var(--text)}
.abs{position:absolute}
/* header */
.site-header{position:absolute;left:0;top:0;width:884px;height:86px;background:#fff}
.brand{left:102px;top:14px;display:flex;align-items:center;gap:9px}
.brand-mark{width:54px;height:54px;border-radius:50%;background:var(--blue)}
.brand-name{font-family:'Lato',sans-serif;font-size:26px;color:var(--green);font-weight:400}
.call{left:658px;top:13px;display:flex;gap:8px;align-items:center}
.call small{display:block;font-size:10px;letter-spacing:1.6px;font-weight:700;color:#333}
.call strong{display:block;font-size:15px;color:#222;font-weight:700}
.nav{left:434px;top:58px;display:flex;gap:11px;font-family:'Arimo',sans-serif;font-weight:700;font-size:11px;color:#222}
.nav .active{color:var(--blue)}
/* hero */
.hero{left:0;top:86px;width:884px;height:419px;background:linear-gradient(100deg,#6e5c44 0%,#a88d65 28%,#1f4fb8 52%,#2a2a2a 75%,#8d8a84 100%)}
.hero-bar{left:0;top:451px;width:884px;height:54px;background:rgba(20,30,50,.6)}
.hero-title{left:103px;top:459px;font-family:'Anton',sans-serif;font-size:24px;color:#fff;letter-spacing:.2px}
.hero-btn{left:514px;top:459px;width:139px;height:38px;border:3px solid #fff;border-radius:20px;background:var(--blue);color:#fff;font-weight:700;font-size:17px;text-align:center;line-height:32px}
.dots{left:697px;top:470px;display:flex;gap:9px}
.dots i{width:15px;height:15px;background:#fff;display:block}
.dots i.on{background:var(--green)}
/* features */
.features{left:0;top:505px;width:884px;height:277px;background:linear-gradient(#fff,#f1f1f1)}
.feature{position:absolute;top:33px;width:215px}
.feature .pic{width:167px;height:95px}
.feature h3{font-family:'Arimo',sans-serif;font-size:12.5px;font-weight:700;color:#222;margin-top:32px}
.feature p{font-size:10px;line-height:14px;margin-top:13px;color:#444}
.feature a{display:block;font-size:10.5px;font-weight:700;color:var(--blue);margin-top:11px;text-decoration:none}
/* band */
.band{left:0;top:782px;width:884px;height:240px;background:var(--band)}
.panel-head{position:absolute;top:18px;display:flex;align-items:center;gap:7px;font-family:'Arimo',sans-serif;font-weight:700;font-size:17px;color:var(--blue)}
.panel-head span{color:var(--green)}
.arrows{position:absolute;top:24px;display:flex;gap:9px}
.arrows i{width:14px;height:14px;border-radius:50%;background:#333;display:block}
.rule{position:absolute;top:48px;border-top:1px dotted #999}
.quote{left:104px;top:842px;width:318px;height:108px;background:#fff;border-radius:7px;padding:10px 14px 0 16px;font-style:italic;font-size:10px;line-height:16.5px;color:#333}
.avatar{left:121px;top:938px;width:58px;height:58px;border-radius:50%;background:#c9a77e;border:3px solid #fff;box-shadow:0 0 0 1px #bbb}
.who{left:221px;top:968px;font-size:10.5px;font-weight:700;color:#333}
.vline{left:441px;top:830px;height:180px;border-left:1px solid #cfcfcf}
.event{position:absolute;left:458px;width:322px;display:flex;gap:9px}
.date{width:23px;text-align:center;font-weight:700}
.date b{display:block;background:#888;color:#fff;font-size:6.5px;line-height:8px}
.date em{display:block;background:#fff;font-style:normal;font-size:8px;line-height:13px;color:#333}
.event h4{font-size:10px;color:var(--blue);font-weight:700}
.event p{font-size:9.5px;line-height:13px;color:#333}
/* footer */
.site-footer{left:0;top:1022px;width:884px;height:152px;background:var(--footer);color:#ddd}
.fcol{position:absolute;top:12px}
.fcol h5{font-size:14px;font-weight:400;color:#fff;padding-bottom:5px;border-bottom:1px solid #555}
.fcol ul{list-style:none;font-size:9.5px;margin-top:8px}
.fcol li{line-height:17.6px}
.fcol li::before{content:"› ";color:#aaa}
.crow{display:flex;gap:10px;font-size:9.5px;line-height:12.5px;margin-top:9px}
.map{width:161px;height:82px;margin-top:8px;border:2px solid #fff;background:linear-gradient(135deg,#e9dcc0,#9fc3e0 60%,#e6d6b0)}
.social li::before{content:none}
.social li{display:flex;align-items:center;gap:10px;line-height:23px}
.social i{width:15px;height:15px;background:#fff;display:block}
.copyright{left:0;top:1174px;width:884px;height:26px;background:var(--footer-bar);color:#fff;font-size:10px;text-align:center;line-height:26px}
</style>
</head>
<body>
<header class="site-header">
  <div class="abs brand"><div class="brand-mark"></div><div class="brand-name">BenefitPorter.com</div></div>
  <div class="abs call">
    <svg width="27" height="27" viewBox="0 0 27 27"><circle cx="13.5" cy="13.5" r="12" fill="none" stroke="#2da84a" stroke-width="2"/><path d="M9 7l3 0 1 4-2 1.5c1 2 2.5 3.5 4.5 4.5L17 15l4 1v3c-7 0-12-5-12-12z" fill="#2da84a"/></svg>
    <div><small>CALL US TODAY</small><strong>123-456-7890</strong></div>
  </div>
  <nav class="abs nav"><span class="active">PRICING</span><span>FEATURES</span><span>SERVICES</span><span>PRODUCTS</span><span>ABOUT</span><span>CONTACT</span></nav>
</header>

<div class="abs hero" role="img" aria-label="Auctioneer in a blue shirt raising a microphone beside donated golf bags"></div>
<div class="abs hero-bar"></div>
<div class="abs hero-title">Sold! Silent Auction Items Add More $!</div>
<div class="abs hero-btn">LEARN MORE</div>
<div class="abs dots"><i class="on"></i><i></i><i></i><i></i></div>

<section class="abs features">
  <div class="feature" style="left:102px">
    <div class="pic" role="img" aria-label="Businessman beside a rising bar chart" style="background:linear-gradient(90deg,#2c3e5c,#7fa3cc,#d6e2ee)"></div>
    <h3>RAISE MORE, STRESS LESS</h3>
    <p>Lorem ipsum dolor si amet consectetur adipiscing elit Etiam feugiat urna leo Lorem ipsum dolor si amet.</p>
    <a>READ MORE »</a>
  </div>
  <div class="feature" style="left:347px">
    <div class="pic" role="img" aria-label="Team of colleagues in a bright office" style="background:linear-gradient(90deg,#8aa3bd,#c9d3dc,#e8ecef)"></div>
    <h3>EVERYTHING YOU NEED</h3>
    <p>Lorem ipsum dolor si amet con adipiscing elit Etiam feugiat urna Lorem ipsum dolor si amet.</p>
    <a>READ MORE »</a>
  </div>
  <div class="feature" style="left:576px">
    <div class="pic" role="img" aria-label="Wooden auction gavel on a desk" style="background:linear-gradient(90deg,#7a4a2c,#c99a6e,#5a301c)"></div>
    <h3>SOLD! SILENT AUCTION MODUCLE</h3>
    <p>Lorem ipsum dolor si amet consloreectetur adipiscing elit Etiam feugiat urlfsaeoena leo Lorem ipsum dolor si amet.</p>
    <a>READ MORE »</a>
  </div>
</section>

<section class="abs band">
  <div class="panel-head" style="left:102px"><svg width="17" height="15" viewBox="0 0 17 15"><path d="M1 1h10v7H5l-3 3V8H1z" fill="#333"/><path d="M12 4h4v7h-1v3l-3-3H7V9h5z" fill="#333"/></svg>Client <span>Testimonials</span></div>
  <div class="arrows" style="left:384px"><i></i><i></i></div>
  <div class="rule" style="left:102px;width:320px"></div>
  <div class="panel-head" style="left:460px"><svg width="18" height="18" viewBox="0 0 18 18"><rect x="1" y="3" width="16" height="14" fill="none" stroke="#333" stroke-width="1.6"/><rect x="1" y="3" width="16" height="4" fill="#333"/><path d="M4 10h10M4 13h10M7 7v10M11 7v10" stroke="#333"/></svg>Seminars <span style="color:var(--blue)">and</span> <span>Events</span></div>
  <div class="arrows" style="left:744px"><i></i><i></i></div>
  <div class="rule" style="left:460px;width:320px"></div>
</section>
<div class="abs quote">“ Lorem ipsum dolor sit amet consetug e sed diay nibh euismodl tincidunt ut laoreet dolore magam er vol wisi enim ad minim veniam quis nostrud exerci tationorem ipsum dolor sit ametee sed diammmy nibh euismd tincidunt ut laoreet dolore magna aliqur volpatl tiidunt ut laoreet dolore magna aliqur volpatl</div>
<div class="abs avatar" role="img" aria-label="Portrait of the client"></div>
<div class="abs who">Mr. Owen Hartley</div>
<div class="abs vline"></div>
<div class="event" style="top:840px"><div class="date"><b>JULY</b><em>23</em></div><div><h4>Duis autem vel eumsodn</h4><p>Lorem ipsum dolor sit ametm nk consectetuer adipiscing elit lorem io Lorem ipsum dolor sit ametm nk consectetuer.</p></div></div>
<div class="event" style="top:899px"><div class="date"><b>JULY</b><em>23</em></div><div><h4>Duis autem vel eumsodn</h4><p>Lorem ipsum dolor sit ametm nk consectetuer adipiscing elit lorem io Lorem ipsum dolor sit ametm nk consectetuer.</p></div></div>
<div class="event" style="top:959px"><div class="date"><b>JULY</b><em>23</em></div><div><h4>Duis autem vel eumsodn</h4><p>Lorem ipsum dolor sit ametm nk consectetuer adipiscing elit lorem io Lorem ipsum dolor sit ametm nk consectetuer.</p></div></div>

<footer class="abs site-footer">
  <div class="fcol" style="left:102px;width:91px"><h5>Quick Links</h5><ul><li>Pricing</li><li>Features</li><li>Services</li><li>Products</li><li>About</li><li>Contact</li></ul></div>
  <div class="fcol" style="left:242px;width:173px"><h5>Contact Information</h5>
    <div class="crow"><svg width="8" height="11" viewBox="0 0 8 11"><path d="M4 0a4 4 0 0 1 4 4c0 3-4 7-4 7S0 7 0 4a4 4 0 0 1 4-4z" fill="#fff"/><circle cx="4" cy="4" r="1.5" fill="#2b2b2b"/></svg><span>Lorem ipsum dolor sit consectetuer adipiscing elit, diam nonummy nibh Street No 5, zip Code: 897410</span></div>
    <div class="crow" style="margin-top:13px"><svg width="9" height="10" viewBox="0 0 9 10"><path d="M1 0h2l1 3-1.5 1c.7 1.5 1.7 2.5 3 3L7 6l2 1v2C4 9 0 5 1 0z" fill="#fff"/></svg><span>123-456-7890</span></div>
    <div class="crow" style="margin-top:13px"><svg width="10" height="8" viewBox="0 0 10 8"><rect width="10" height="8" fill="#fff"/><path d="M0 0l5 4 5-4" stroke="#2b2b2b" fill="none"/></svg><span>hello@benefitporter.net</span></div>
  </div>
  <div class="fcol" style="left:467px;width:161px"><h5>Location Map</h5><div class="map" role="img" aria-label="Street map showing the office location"></div><div style="font-size:9px;margin-top:6px">View Location »</div></div>
  <div class="fcol" style="left:678px;width:90px"><h5>Follow Us</h5><ul class="social"><li><i></i>Friendbook</li><li><i></i>Chirper</li><li><i></i>Circles+</li><li><i></i>Linkwork</li></ul></div>
</footer>
<div class="abs copyright">© 2014 BenefitPorter &nbsp;|&nbsp; All rights reserved</div>
</body>
</html>
```